Fun family flyer for photographer

Need a flyer to promote our business moving to Brisbane.

Require a family friendly look targetted to mothers, using our logo and existing images from previous shoots.

Would like to see designs that feature the images heavily, but still have text and fonts that set it aside from other flyers.
Updates

I would like to see some unique fonts being used, so far I have only recieved "canned" fonts, some were just straight out Adobe fonts (on a design site? Really?).

Some SUGGESTIONS would include font use similar to the following:
http://www.glyphbarn.net/oldmarquee.font
http://www.glyphbarn.net/giddy-otter.font

Fun fonts, something that grabs attention.
If you're going to plonk one image in the middle of the page and fill it with text in Courier New, consider not submitting.

I would like colourful, attention grabbing backgrounds.

Target Market(s)

Families

Industry/Entity Type

Business

Requirements
Must have
• Two sides to the flyer
Focus on "fun"
Targetted to mothers
Nice to have
• All photos attached, not necessary but nice.
Should not have
• Anything too "corporate"

```html
<!DOCTYPE html>
<html lang="en">
<head>
<meta charset="utf-8">
<title>Brightfield Photography – Family Flyer</title>
<link rel="stylesheet" href="https://fonts.googleapis.com/css2?family=Cherry+Cream+Soda&family=Chewy&family=Sniglet:wght@400;800&family=Nunito:ital,wght@0,400;1,600&display=block">
<style>
  :root {
    --paper: #ffffff;
    --ink: #111111;
    --panel-pink: #f9c1f7;
    --ribbon-blue: #2bc3ea;
    --ribbon-blue-dark: #1591b8;
    --ribbon-tan: #e8c993;
    --ribbon-tan-dark: #b48a4f;
    --gold: #c9a052;
    --gold-dark: #5b4320;
    --display: "Cherry Cream Soda", "Chewy", "Sniglet", sans-serif;
  }
  * { box-sizing: border-box; margin: 0; padding: 0; }
  html, body { width: 1200px; height: 900px; overflow: hidden; background: var(--paper); }
  .flyer { position: relative; width: 1200px; height: 900px; background: var(--paper); overflow: hidden; }

  .ornament {
    position: absolute; left: 0; top: 0; width: 175px; height: 900px;
    background: radial-gradient(ellipse at 40% 30%, #e9d39a 0%, #b8904a 35%, rgba(80,60,30,0.55) 60%, rgba(255,255,255,0) 80%);
    opacity: 0.7;
  }

  .photo-strip {
    position: absolute; left: 108px; top: 0; width: 967px; height: 298px;
    display: flex; box-shadow: 0 6px 14px rgba(0,0,0,0.35);
  }
  .photo { flex: 1; height: 100%; }
  .photo--beach { background: linear-gradient(180deg, #b9c2b8 0%, #c9b6a6 60%, #d9a98e 100%); }
  .photo--turtle { background: linear-gradient(180deg, #8a7770 0%, #6f5e58 50%, #a9b3c8 100%); }
  .photo--garden { background: linear-gradient(180deg, #3d6a2c 0%, #6f7b4d 50%, #3b3430 100%); }
  .photo--park { background: radial-gradient(circle at 60% 15%, #fbf4e6 0%, #c7b9a4 35%, #6f7456 80%); }

  .title-ribbon { position: absolute; left: 10px; top: 296px; width: 1180px; height: 100px; }
  .title {
    position: absolute; left: 90px; top: 298px; width: 1020px; height: 82px;
    display: flex; align-items: center; justify-content: center;
    font-family: "Sniglet", sans-serif; font-weight: 400; font-size: 60px; color: var(--paper);
    -webkit-text-stroke: 3px var(--ink); paint-order: stroke fill;
    text-shadow: 3px 3px 0 var(--ink);
    letter-spacing: 1px;
  }

  .panel {
    position: absolute; left: 140px; top: 380px; width: 905px; height: 412px;
    background: var(--panel-pink);
    box-shadow: 4px 6px 12px rgba(0,0,0,0.4);
    text-align: center; padding-top: 30px;
  }
  .panel p { font-family: var(--display); color: var(--ink); text-transform: uppercase; }
  .panel .intro {
    font-size: 19px; line-height: 24px; white-space: nowrap;
    text-shadow: 0 0 3px #fff, 0 0 3px #fff, 0 0 4px #fff;
  }
  .panel .pitch {
    margin-top: 24px; padding: 0 10px; font-size: 31px; line-height: 38px;
    text-shadow: 0 0 3px #fff, 0 0 4px #fff, 0 0 5px #fff, 0 0 6px #fff;
  }

  .brand-mark {
    position: absolute; left: 1045px; top: 700px; width: 130px;
    display: flex; flex-direction: column; align-items: center; gap: 6px;
    font-family: var(--display); font-size: 16px; color: var(--ink);
  }
  .brand-mark .square { width: 40px; height: 40px; background: var(--ink); }

  .contact-ribbon { position: absolute; left: 0; top: 778px; width: 1200px; height: 100px; }
  .contacts {
    position: absolute; left: 112px; top: 795px; width: 968px; height: 64px;
    display: flex; justify-content: space-around; align-items: center; text-align: center;
    font-family: "Nunito", sans-serif; color: var(--ink);
  }
  .contact .label { font-style: italic; font-weight: 600; font-size: 17px; }
  .contact .value { font-size: 18px; }
</style>
</head>
<body>
<main class="flyer">
  <div class="ornament" role="img" aria-label="Gold scrolling flourish ornament down the left edge"></div>

  <section class="photo-strip">
    <div class="photo photo--beach" role="img" aria-label="Photo of a smiling young girl at the beach"></div>
    <div class="photo photo--turtle" role="img" aria-label="Photo of a toddler sitting by a turtle sculpture"></div>
    <div class="photo photo--garden" role="img" aria-label="Photo of a mother with two children in a garden"></div>
    <div class="photo photo--park" role="img" aria-label="Photo of three women outdoors in sunlight"></div>
  </section>

  <svg class="title-ribbon" viewBox="0 0 1180 100" aria-hidden="true">
    <polygon points="0,18 100,18 100,88 0,88 30,53" fill="var(--ribbon-blue-dark)"/>
    <polygon points="1180,18 1080,18 1080,88 1180,88 1150,53" fill="var(--ribbon-blue-dark)"/>
    <rect x="80" y="2" width="1020" height="80" rx="4" fill="var(--ribbon-blue)"/>
    <rect x="80" y="2" width="1020" height="20" fill="#ffffff" opacity="0.25"/>
  </svg>
  <h1 class="title">Brightfield Photography</h1>

  <section class="panel">
    <p class="intro">Thinking about updating the family portrait? Don't have a family portrait?<br>Want a fresh, outdoor shoot rather than an indoor studio?</p>
    <p class="pitch">It would be Brightfield's pleasure to capture or update your family portrait with something modern, fresh and candid. Afterwards you can receive your hi-res images on online, as prints, canvas anything you can think of as the options are endless, the choice is yours!</p>
  </section>

  <div class="brand-mark"><span class="square"></span><span>Brightfield</span></div>

  <svg class="contact-ribbon" viewBox="0 0 1200 100" aria-hidden="true">
    <polygon points="0,8 150,8 150,72 0,72 40,40" fill="var(--ribbon-tan-dark)"/>
    <polygon points="1200,28 1050,28 1050,92 1200,92 1160,60" fill="var(--ribbon-tan-dark)"/>
    <rect x="112" y="14" width="968" height="70" rx="6" fill="var(--ribbon-tan)" stroke="var(--gold-dark)" stroke-width="3"/>
  </svg>
  <footer class="contacts">
    <div class="contact"><div class="label">Website:</div><div class="value">http://brightfieldphoto.com.au/</div></div>
    <div class="contact"><div class="label">Phone:</div><div class="value">040-555-0127</div></div>
    <div class="contact"><div class="label">Email:</div><div class="value">hello@brightfieldphoto.com.au</div></div>
  </footer>
</main>
</body>
</html>
```